Brindexa Business Card

Our mission is to craft high value solutions combining consulting and edge technologies for helping big and middle sized companies in the Digital Transformation Process that they must face. We think that this transformation will impact business processes and people skills in a new manner. Brindexa's value proposition is to collaborate with our clients for creating new competitive advantages based on technology, processes and people.
We already have a logo designed through your platform.

Industry/Entity Type

Business

```html
<!DOCTYPE html>
<html lang="en">
<head>
<meta charset="utf-8">
<title>Brindexa Business Card</title>
<link rel="stylesheet" href="https://fonts.googleapis.com/css2?family=Questrial&display=swap">
<style>
  :root {
    --page: #e9eaea;
    --card-white: #f7f7f6;
    --card-black: #1b1b1b;
    --brand-blue: #0a86c6;
    --light-blue: #5bbbe6;
    --soft-grey: #c4c4c4;
    --ink: #111111;
    --paper-white: #ffffff;
  }
  * { box-sizing: border-box; margin: 0; padding: 0; }
  html, body {
    width: 1200px; height: 1000px; overflow: hidden;
    background: var(--page);
    font-family: "Questrial", sans-serif;
  }
  .canvas { position: relative; width: 1200px; height: 1000px; }
  .card {
    position: absolute; left: 250px; width: 700px; height: 400px;
    overflow: hidden; box-shadow: 0 6px 18px rgba(0,0,0,.12);
  }
  .card--back { top: 60px; background: var(--card-black); display: flex; align-items: center; justify-content: center; }
  .card--front { top: 520px; background: var(--card-white); }

  .brand { display: flex; align-items: center; gap: 14px; letter-spacing: .06em; text-transform: uppercase; }
  .brand__dot { border-radius: 50%; background: var(--brand-blue); flex: none; }
  .card--back .brand { color: var(--paper-white); font-size: 52px; }
  .card--back .brand__dot { width: 54px; height: 54px; }

  .front__decor { position: absolute; left: -150px; top: -40px; width: 440px; height: 440px; }

  .front__info { position: absolute; right: 48px; top: 58px; width: 330px; text-align: right; }
  .card--front .brand { justify-content: flex-end; color: var(--ink); font-size: 30px; }
  .card--front .brand__dot { width: 32px; height: 32px; }
  .person { margin-top: 40px; }
  .person__name { color: var(--brand-blue); font-size: 36px; line-height: 1; }
  .person__role { color: var(--ink); font-size: 20px; letter-spacing: .08em; margin-top: 2px; }
  .contacts { list-style: none; margin-top: 24px; }
  .contacts li {
    display: flex; justify-content: flex-end; align-items: center; gap: 14px;
    font-size: 22px; letter-spacing: .1em; color: var(--ink); line-height: 30px;
  }
  .contacts svg { width: 18px; height: 18px; flex: none; }
</style>
</head>
<body>
<main class="canvas">
  <section class="card card--back" aria-label="Card back">
    <div class="brand"><span class="brand__dot"></span>Brindexa</div>
  </section>

  <section class="card card--front" aria-label="Card front">
    <svg class="front__decor" viewBox="0 0 440 440" aria-hidden="true">
      <circle cx="220" cy="220" r="205" fill="none" stroke="var(--soft-grey)" stroke-width="22"/>
      <circle cx="220" cy="220" r="170" fill="none" stroke="var(--brand-blue)" stroke-width="36"/>
    </svg>

    <div class="front__info">
      <div class="brand"><span class="brand__dot"></span>Brindexa</div>
      <div class="person">
        <p class="person__name">Your Name</p>
        <p class="person__role">POSITION</p>
      </div>
      <ul class="contacts">
        <li>000 000 000
          <svg viewBox="0 0 24 24" aria-label="Phone"><path d="M6 3l3 4-2 2c1 3 4 6 7 7l2-2 4 3-2 3C10 20 4 14 3 6z" fill="none" stroke="var(--brand-blue)" stroke-width="2"/></svg>
        </li>
        <li>000 000 000
          <svg viewBox="0 0 24 24" aria-label="Mobile"><rect x="7" y="2" width="10" height="20" rx="2" fill="none" stroke="var(--brand-blue)" stroke-width="2"/><line x1="10" y1="18" x2="14" y2="18" stroke="var(--brand-blue)" stroke-width="2"/></svg>
        </li>
        <li>000@000000
          <svg viewBox="0 0 24 24" aria-label="Email"><rect x="2" y="5" width="20" height="14" fill="none" stroke="var(--brand-blue)" stroke-width="2"/><path d="M2 5l10 8 10-8" fill="none" stroke="var(--brand-blue)" stroke-width="2"/></svg>
        </li>
        <li>www.0000000000
          <svg viewBox="0 0 24 24" aria-label="Website"><path d="M5 2l14 12-6 1 4 7-3 1-4-7-5 4z" fill="none" stroke="var(--brand-blue)" stroke-width="2"/></svg>
        </li>
      </ul>
    </div>
  </section>
</main>
</body>
</html>
```